Business Card Design for Law firm - already have logo

Now that we have a logo, we need a business card design - our logo is attached -it is salaryman font if that helps - we would like a file that can be uploaded to cardquill (www.cardquill-example.com) using the logo and with the following information on it:
Quenby Law Firm, P.C.
Delwyn Quenby, Esq.
5817 SW 19th Ave.
Portland, OR 97213
971.555.0142 phone
971.555.0187 fax
del@quenby-example.net
Skype: delquenby
Google talk: delwyn.quenby@mailbox-example.com
Target Market(s)
our business cards are distributed to corporate executives, technology professionals and healthcare providers
Industry/Entity Type
Business
Look and feel

```html
<!DOCTYPE html>
<html lang="en">
<head>
<meta charset="utf-8">
<title>Quenby Law Firm – Business Card</title>
<link rel="stylesheet" href="https://fonts.googleapis.com/css2?family=Michroma&family=Roboto:wght@400;500&display=swap">
<style>
  :root {
    --backdrop: #c9c9cb;
    --paper: #ffffff;
    --ink: #1a1a1a;
    --ink-soft: #3a3a3a;
    --card-black: #080808;
    --tick: #f2f2f2;
    --url-grey: #9a9a9a;
  }
  * { box-sizing: border-box; margin: 0; padding: 0; }
  html, body { width: 1200px; height: 900px; overflow: hidden; }
  body {
    background: radial-gradient(ellipse at 50% 40%, #dcdcde 0%, var(--backdrop) 70%, #b4b4b6 100%);
    position: relative;
    font-family: "Roboto", Arial, sans-serif;
    color: var(--ink);
  }
  .card {
    position: absolute;
    left: 337px;
    width: 525px;
    height: 300px;
    box-shadow: 0 6px 18px rgba(0,0,0,.18);
  }
  /* Front */
  .card-front { top: 110px; background: var(--paper); text-align: center; padding-top: 34px; }
  .firm-name {
    font-family: "Michroma", sans-serif;
    font-size: 21px;
    font-weight: 400;
    letter-spacing: 3px;
    text-transform: uppercase;
    color: var(--ink);
  }
  .person { margin-top: 16px; font-size: 17px; font-weight: 500; }
  .title { font-size: 10px; color: var(--ink-soft); margin-top: 1px; }
  .address { margin-top: 12px; font-size: 12px; line-height: 1.25; color: var(--ink-soft); }
  .phones { margin-top: 8px; font-size: 12px; color: var(--ink-soft); }
  .email { font-size: 12px; color: var(--ink-soft); }
  .chat-row {
    margin-top: 10px;
    display: flex; justify-content: center; gap: 22px;
    font-size: 11.5px; color: var(--ink-soft);
  }
  .chat-item { display: flex; align-items: center; gap: 5px; }
  .chat-mark { width: 10px; height: 10px; background: var(--ink); display: inline-block; }
  .front-brand {
    margin-top: 12px;
    display: flex; justify-content: center; align-items: center; gap: 6px;
    font-size: 13px; font-weight: 500; color: var(--ink);
  }
  .brand-square { width: 10px; height: 10px; background: var(--ink); display: inline-block; }
  /* Back */
  .card-back { top: 470px; background: var(--card-black); overflow: hidden; }
  .edge-ticks { position: absolute; left: 0; top: 0; }
  .back-brand {
    position: absolute; left: 0; right: 0; top: 112px;
    display: flex; justify-content: center; align-items: center; gap: 14px;
    font-size: 44px; font-weight: 500;
    color: var(--paper);
  }
  .back-square { width: 26px; height: 26px; background: var(--paper); display: inline-block; }
  .back-url {
    position: absolute; left: 0; right: 0; top: 196px;
    text-align: center;
    font-family: "Michroma", sans-serif;
    font-size: 11px;
    letter-spacing: 5px;
    color: var(--url-grey);
    text-transform: uppercase;
  }
</style>
</head>
<body>
  <section class="card card-front">
    <h1 class="firm-name">Quenby Law Firm, P.C.</h1>
    <p class="person">Delwyn Quenby,</p>
    <p class="title">Esq.</p>
    <p class="address">5817 SW 19th Ave.<br>Portland, OR 97213</p>
    <p class="phones">PH: 971.555.0142 / FAX: 971.555.0187</p>
    <p class="email">del@quenby-example.net</p>
    <div class="chat-row">
      <span class="chat-item"><span class="chat-mark"></span>delquenby</span>
      <span class="chat-item"><span class="chat-mark"></span>delwyn.quenby@mailbox-example.com</span>
    </div>
    <div class="front-brand"><span class="brand-square"></span>Quenby</div>
  </section>

  <section class="card card-back">
    <svg class="edge-ticks" width="525" height="300" viewBox="0 0 525 300" aria-hidden="true">
      <g fill="var(--tick)">
        <rect x="22" y="0" width="30" height="7"/><rect x="82" y="0" width="30" height="7"/>
        <rect x="142" y="0" width="30" height="7"/><rect x="202" y="0" width="30" height="7"/>
        <rect x="262" y="0" width="30" height="7"/><rect x="322" y="0" width="30" height="7"/>
        <rect x="382" y="0" width="30" height="7"/><rect x="442" y="0" width="30" height="7"/>
        <rect x="22" y="293" width="30" height="7"/><rect x="82" y="293" width="30" height="7"/>
        <rect x="142" y="293" width="30" height="7"/><rect x="202" y="293" width="30" height="7"/>
        <rect x="262" y="293" width="30" height="7"/><rect x="322" y="293" width="30" height="7"/>
        <rect x="382" y="293" width="30" height="7"/><rect x="442" y="293" width="30" height="7"/>
      </g>
    </svg>
    <div class="back-brand"><span class="back-square"></span>Quenby</div>
    <p class="back-url">www.quenby-example.net</p>
  </section>
</body>
</html>
```